Fact Sheets for Insurance

We need a 4 page booklet brochure designed for our insurance business. Each page is A4. We design insurance plans for our Clients and we wish to use the brochure to market and educate our Client and business partners. The business is Halvard Mensley Financial Services. Colour scheme of our logo and stationary is navy blue and metallic gold. The content has been drafted and each page is attached. Please use your creative freedom to make it look professional and modern. We would like graphics, pictures etc to make it more vibrant as well.

Industry/Entity Type

Insurance

```html
<!DOCTYPE html>
<html lang="en">
<head>
<meta charset="utf-8">
<title>Cheat Sheet - Buying TPD Insurance | Halvard Mensley Financial Services</title>
<link href="https://fonts.googleapis.com/css2?family=Anton&family=Roboto+Condensed:wght@400;700&family=Open+Sans:wght@300;400&display=swap" rel="stylesheet">
<style>
:root{
  --navy:#1b4675;
  --navy-deep:#173c66;
  --blue:#2a64a0;
  --gold:#a8965c;
  --gold-light:#b9a76b;
  --ink-blue:#1d55a0;
  --white:#ffffff;
  --paper:#f4f4f4;
}
*{margin:0;padding:0;box-sizing:border-box}
html,body{width:850px;height:1200px;overflow:hidden;background:var(--white)}
.sheet{position:relative;width:850px;height:1200px;overflow:hidden;font-family:"Roboto Condensed",sans-serif}
.masthead{position:absolute;left:0;top:0;width:850px;height:190px;background:linear-gradient(180deg,var(--navy-deep),var(--navy));display:flex;align-items:center;justify-content:center;border-bottom:2px solid #d9d9d9}
.masthead h1{font-family:"Anton",sans-serif;font-weight:400;color:var(--white);font-size:45px;line-height:57px;text-align:center;letter-spacing:.3px}
.hero{position:absolute;left:0;top:192px;width:850px;height:568px;background:radial-gradient(ellipse at 35% 55%,#d8d8d8 0%,#f0f0f0 40%,var(--paper) 70%)}
.tab{position:absolute;height:20px;background:var(--gold);color:var(--white);font-size:13px;line-height:20px;padding-left:12px;border-radius:10px 0 0 0}
.tab.need{left:530px;top:195px;width:320px;padding-left:44px}
.tab.who{left:530px;top:475px;width:320px;text-align:center;padding-left:0}
.needs{position:absolute;left:568px;top:222px;width:262px;border-collapse:collapse;font-size:13px}
.needs th{background:var(--navy);color:var(--white);font-weight:400;height:19px;text-align:center}
.needs td{height:19px;color:#10213a;padding-left:5px;vertical-align:top;line-height:19px}
.needs tr.shade td{background:var(--gold-light);color:var(--ink-blue)}
.needs td.amt{color:var(--ink-blue);width:111px;padding-left:2px}
.providers{position:absolute;left:597px;top:505px;list-style:none;font-size:13px;line-height:17.5px;color:var(--ink-blue)}
.providers li::before{content:"";display:inline-block;width:5px;height:5px;border-radius:50%;background:var(--gold);margin-right:7px;vertical-align:2px}
.lower{position:absolute;left:0;top:760px;width:850px;height:440px;background:linear-gradient(180deg,var(--navy) 0%,var(--blue) 75%,var(--navy) 100%)}
.band{position:absolute;top:762px;height:18px;background:var(--gold);color:var(--white);font-size:13px;line-height:18px}
.band.tips{left:0;width:458px;padding-left:40px}
.band.adviser{left:460px;width:390px;padding-left:10px}
.checks{position:absolute;list-style:none;color:var(--white);font-size:12px;line-height:17px;letter-spacing:-.3px}
.checks li{position:relative;padding-left:24px;margin-bottom:1px}
.checks svg{position:absolute;left:0;top:2px;width:14px;height:14px}
.checks .hl{color:var(--gold-light)}
.checks.tips{left:16px;top:811px;width:405px}
.adviser-lead{position:absolute;left:470px;top:792px;color:var(--gold-light);font-size:12px;letter-spacing:-.3px}
.checks.adviser{left:446px;top:811px;width:390px}
.adviser-note{position:absolute;left:470px;top:897px;width:370px;color:var(--white);font-size:12px;line-height:17px;letter-spacing:-.3px}
.brand{position:absolute;left:612px;top:982px;width:225px;text-align:center;color:var(--white);font-family:"Open Sans",sans-serif;font-weight:400}
.brand .mark{display:block;width:34px;height:34px;border:2px solid var(--gold);margin:0 auto 8px}
.brand .name{display:block;font-size:15px;letter-spacing:1px;line-height:20px}
.disclaimer{position:absolute;left:330px;top:1094px;color:#d6e0ec;font-family:"Open Sans",sans-serif;font-weight:300;font-size:13px}
.rule{position:absolute;left:0;top:1124px;width:850px;height:2px;background:#c8d3e0}
.pillar{position:absolute;top:1131px;font-family:"Open Sans",sans-serif}
.pillar .word{display:block;color:var(--gold);font-weight:300;font-size:25px;letter-spacing:8px}
.pillar .line{display:block;color:var(--white);font-size:11.5px;letter-spacing:.6px;margin-top:-1px}
.pillar.one{left:12px}
.pillar.two{left:340px}
.pillar.three{left:627px}
</style>
</head>
<body>
<div class="sheet">
  <header class="masthead">
    <h1>Cheat Sheet - Buying Total and<br>Permanent Disability (TPD) Insurance</h1>
  </header>

  <div class="hero" role="img" aria-label="Photograph: a woman with a prosthetic leg sits on a white chair, head bowed, silhouetted against a bright studio background"></div>

  <div class="tab need">How Much Do I need?</div>
  <table class="needs">
    <tr><th>Need</th><th>Amount</th></tr>
    <tr class="shade"><td>Repaying Debts</td><td class="amt">$</td></tr>
    <tr><td>Medical Expenses</td><td class="amt">$</td></tr>
    <tr class="shade"><td>Home Modification<br>Costs</td><td class="amt">$</td></tr>
    <tr><td>Other</td><td class="amt">$</td></tr>
    <tr class="shade"><td>TOTAL</td><td class="amt">$</td></tr>
  </table>

  <div class="tab who">Who offers it?</div>
  <ul class="providers">
    <li>Most Superannuation Funds</li>
    <li>Some Private Health Funds</li>
    <li>Some Employers</li>
    <li>Life Insurance Companies</li>
    <li>General Insurance Companies</li>
  </ul>

  <section class="lower"></section>
  <div class="band tips">Tips &amp; Traps</div>
  <div class="band adviser">When to call a Professional Adviser?</div>

  <svg width="0" height="0" style="position:absolute">
    <symbol id="tick" viewBox="0 0 14 14"><rect x="1" y="2" width="11" height="11" fill="none" stroke="#fff" stroke-width="1.3"/><path d="M3.5 7.5l2.5 2.5 6.5-8" fill="none" stroke="#fff" stroke-width="1.6"/></symbol>
  </svg>

  <ul class="checks tips">
    <li><svg><use href="#tick"/></svg><span class="hl">Purchase an "Own Occuation" definition Policy</span> to ensure that you are not tested against your ability to work in "Any Occupation" at claim time.</li>
    <li><svg><use href="#tick"/></svg><span class="hl">Review what the policy doesn't cover "Exclusions".</span> Standard exclusion for most policies is self-inflicted acts.</li>
    <li><svg><use href="#tick"/></svg>Look to <span class="hl">purchase "Long Term" Life Insurance</span> if you think you will need to hold the policy for a number of years. This may save you tens of thousands of dollars over the life of your policy.</li>
    <li><svg><use href="#tick"/></svg>Ensure the contract is <span class="hl">guaranteed to be renewed</span> if you pay your premiums until expiry age.</li>
    <li><svg><use href="#tick"/></svg>If purchased through Super, <span class="hl">you may be liable for a tax bill</span> in the event of a claim.</li>
  </ul>

  <p class="adviser-lead">If you need help:</p>
  <ul class="checks adviser">
    <li><svg><use href="#tick"/></svg>comparing premiums</li>
    <li><svg><use href="#tick"/></svg>reviewing &amp; comparing policy terms and conditions</li>
    <li><svg><use href="#tick"/></svg>matching a policy to suit your occupation</li>
    <li><svg><use href="#tick"/></svg>purchasing "Long Term" Life Insurance</li>
  </ul>
  <p class="adviser-note">If you want to ensure that you have someone assisting you if a claim is ever needed to be made.</p>

  <div class="brand">
    <span class="mark"></span>
    <span class="name">Halvard Mensley<br>Financial Services</span>
  </div>

  <p class="disclaimer">Corporate Authorised Representative of Northvale Advisory Partners AFSL 408215</p>
  <div class="rule"></div>

  <div class="pillar one"><span class="word">CERTAINTY</span><span class="line">DESIGNING INSURANCE SOLUTIONS</span></div>
  <div class="pillar two"><span class="word">CLARITY</span><span class="line">STRATEGIC PLANNING ADVICE</span></div>
  <div class="pillar three"><span class="word">CONFIDENCE</span><span class="line">CONSTRUCTING RETIREMENT PLANS</span></div>
</div>
</body>
</html>
```